FotoVELTA buisnesscard

Hey :) I need a modern buisnesscard for my company FotoVELTA
It most have:
Dagligleder og Fotograf: Henrik Torvald Bjelland

Mob: +4791642058
Epost: post@fotovelta.no
Adresse: Bakkestien22, 6090 Fjordvik

Facbook and instagram logo with text FotoVELTA

FotoVELTA logo

It Company

```html
<!DOCTYPE html>
<html lang="no">
<head>
<meta charset="utf-8">
<title>FotoVELTA – visittkort</title>
<link href="https://fonts.googleapis.com/css2?family=Open+Sans:wght@400;600;700;800&display=swap" rel="stylesheet">
<style>
  :root {
    --bg: #2c2c2e;
    --card: #ffffff;
    --blue: #1173bb;
    --pink: #c4467f;
    --text-light: #ffffff;
  }
  * { box-sizing: border-box; margin: 0; padding: 0; }
  html, body {
    width: 1200px; height: 1200px; overflow: hidden;
    background: var(--bg);
    font-family: "Open Sans", Arial, sans-serif;
  }
  .stage {
    width: 1200px; height: 1200px;
    display: flex; flex-direction: column; align-items: center; justify-content: center;
    gap: 60px;
  }
  .card {
    position: relative;
    width: 940px; height: 520px;
    border-radius: 40px;
    background: var(--card);
    overflow: hidden;
  }
  .brand-name {
    font-family: "Open Sans", Arial, sans-serif;
    font-weight: 800;
    color: var(--blue);
    letter-spacing: -1px;
    line-height: 1;
  }

  /* Front */
  .front .brand-name {
    position: absolute; left: 0; right: 0; top: 170px;
    text-align: center; font-size: 96px;
  }
  .front .pink-rule {
    position: absolute; left: 0; right: 0; bottom: 84px; height: 16px;
    background: var(--pink);
  }
  .front .social-band {
    position: absolute; left: 0; right: 0; bottom: 0; height: 84px;
    background: var(--blue);
    display: flex; align-items: center; justify-content: center; gap: 34px;
  }
  .social-handle {
    display: flex; align-items: center; gap: 9px;
    color: var(--text-light); font-size: 20px; font-weight: 400;
  }
  .social-handle .mark {
    width: 18px; height: 18px; border-radius: 3px; background: var(--text-light);
  }

  /* Back */
  .back { background: var(--blue); }
  .back .shape { position: absolute; inset: 0; }
  .back .brand-name {
    position: absolute; left: 30px; width: 480px; top: 225px;
    text-align: center; font-size: 76px;
  }
  .contact {
    position: absolute; left: 625px; top: 110px;
    color: var(--text-light);
  }
  .contact .person { font-size: 24px; font-weight: 700; white-space: nowrap; }
  .contact .role { font-size: 19px; margin-top: 2px; }
  .contact .address { font-size: 19px; line-height: 1.35; margin-top: 26px; }
  .contact .lines { margin-top: 26px; font-size: 19px; line-height: 1.45; }
  .contact .line { display: flex; align-items: center; gap: 12px; }
  .contact .line svg { width: 18px; height: 18px; flex: none; }
</style>
</head>
<body>
<main class="stage">

  <section class="card front" aria-label="Visittkort forside">
    <div class="brand-name">FotoVELTA</div>
    <div class="pink-rule"></div>
    <div class="social-band">
      <span class="social-handle"><span class="mark"></span>/FotoVELTA</span>
      <span class="social-handle"><span class="mark"></span>@FotoVELTA</span>
    </div>
  </section>

  <section class="card back" aria-label="Visittkort bakside">
    <svg class="shape" viewBox="0 0 940 520" preserveAspectRatio="none" aria-hidden="true">
      <path d="M0 0 H360 C560 60 620 260 580 520 H0 Z" fill="var(--pink)"/>
      <path d="M0 0 H330 C522 62 580 262 542 520 H0 Z" fill="var(--card)"/>
    </svg>
    <div class="brand-name">FotoVELTA</div>
    <div class="contact">
      <div class="person">Henrik Torvald Bjelland</div>
      <div class="role">Dagligleder og Fotograf</div>
      <div class="address">Bakkestien22,<br>6090 Fjordvik</div>
      <div class="lines">
        <div class="line">
          <svg viewBox="0 0 24 24" aria-hidden="true"><path fill="#fff" d="M6.6 10.8a15.1 15.1 0 0 0 6.6 6.6l2.2-2.2c.3-.3.7-.4 1-.2 1.1.4 2.3.6 3.6.6.6 0 1 .4 1 1V20c0 .6-.4 1-1 1A17 17 0 0 1 3 4c0-.6.4-1 1-1h3.5c.6 0 1 .4 1 1 0 1.3.2 2.5.6 3.6.1.3 0 .7-.2 1z"/></svg>
          <span>+4791642058</span>
        </div>
        <div class="line">
          <svg viewBox="0 0 24 24" aria-hidden="true"><path fill="#fff" d="M3 5h18c.6 0 1 .4 1 1v12c0 .6-.4 1-1 1H3c-.6 0-1-.4-1-1V6c0-.6.4-1 1-1zm9 7.5L20 7H4z"/></svg>
          <span>post@fotovelta.no</span>
        </div>
      </div>
    </div>
  </section>

</main>
</body>
</html>
```